依頼詳細
現在木曜日のみ休診となっていますが、獣医が一人増えることにより2020年2月1日より全曜日で診察を行うことを予定しています(盆、年末年始、GW除く)。
その告知をするためのチラシをポスティング、新聞折り込みで配布する予定で、その告知チラシのデザインをお願いしたいです。表面は動物病院の告知で、裏面は併設のトリミングサロンの宣伝をしたいと思っています。思わず引きつかれるようなデザインをお願いしたいです。
(表面)
・添付のミドリツバメ便の画像のイメージで「木曜日休診」が「全曜日診察」(盆、年末年始、GWは除く)へ変わることを告知したいです
・キャラクターは犬と猫のイラストでお願いしたいです
・全体的なデザインはシンプルで遊び心があるものにしてほしいです
・看板(暖簾)の写真(添付)も載せてほしいです(これは小さくてよいです)
(裏面)
・犬が猫足バスタブに浸かって、楽しそうにしているイメージでお願いします
・こちらもシンプルで遊び心のあるデザインでお願いしたいです
・トリミングは「シャンプーのみ」、「シャンプー&カット」のコースがあり、両コースに爪切り、足裏バリカン、耳掃除、お腹バリカン、肛門バリカン、肛門嚢絞りを含むことを記載してほしいです
・動物病院併設なのでシニア犬、持病持ちの犬も対応可能と載せてほしいです
・看板(暖簾)の写真(添付)も載せてほしいです(これも小さくてよいです)
記載項目
【表面】
動物病院ひだまり 若草台
京都市西京区小川原南町17 メゾン葵野2階
電話番号 0756147328
診察時間 午前9:30~12:30 予約診察16:00~16:45 午後17:00~20:00
(日、祝日は午前のみ)
全曜日診察(盆、正月、GWは除く)
獣医師名 院長 青柳航平 副院長 村瀬譲
駐車場5台完備(トリミングサロン共用)
駐車場地図(添付)
【裏面】
トリミングサロン凛(動物病院ひだまり 若草台 併設)
電話番号 0756281945
営業時間 9:00~18:00
店休日 木曜日 日曜日
店長名 北條葉月
駐車場5台完備(動物病院共用)
ペットホテル完備
トリミング料金 (税抜き)
・トイプードル シャンプー3780円~ シャンプー&カット6480円~
・チワワ シャンプー2980円~ シャンプー&カット4480円~
・ヨークシャーテリア シャンプー3280円~ シャンプー&カット5780円~
その他全犬種対応可能
ペットホテル料金(1泊2日、税抜き)
・小型犬 2980円 ・中型犬 3980円 ・大型犬 4980円
一時預かりも可能
サイズ
A3
ページ数
両面
希望イメージ
シンプル 複雑
単色 カラフル
暗い 明るい
日常 高級
遊び心 厳粛
未来的 伝統的
女性的 男性的
希望する色
黄・オレンジ系、緑系、茶系
納品ファイル
補足説明
手直しのやり取りは基本的に少なく(5回以下に)したいと思いますが、納得のいくものを制作していただきたいので、出来れば制限を設けないようにしてもらいたいです

診察表を使った表現が、病院であることが分かりやすく気に入りました。

この度はコンペに応募していただきありがとうございました。

```html
<!DOCTYPE html>
<html lang="ja">
<head>
<meta charset="utf-8">
<title>動物病院ひだまり 若草台からお知らせ</title>
<link href="https://fonts.googleapis.com/css2?family=M+PLUS+Rounded+1c:wght@500;700;800&display=swap" rel="stylesheet">
<style>
  :root {
    --green: #7fb63a;
    --green-dark: #4f8a1f;
    --orange: #f29a2e;
    --red: #e2452c;
    --pink: #fbe2d8;
    --cream: #fff9ef;
    --ink: #3b2a1c;
    --brown: #8a5a33;
    --white: #ffffff;
  }
  * { margin: 0; padding: 0; box-sizing: border-box; }
  html, body { width: 849px; height: 1200px; overflow: hidden; }
  body {
    font-family: "M PLUS Rounded 1c", sans-serif;
    color: var(--ink);
    background: var(--white);
  }
  .flyer { position: relative; width: 849px; height: 1200px; overflow: hidden;
    background: linear-gradient(180deg, var(--pink) 0%, #fdeee6 57%, var(--white) 59%); }

  .art { position: absolute; border-radius: 40%; }
  .art-dog { left: 100px; top: 50px; width: 240px; height: 250px;
    background: radial-gradient(circle at 50% 50%, #e8a45a 0%, #c9803c 55%, transparent 70%); }
  .art-cat-right { right: 40px; top: 410px; width: 170px; height: 175px;
    background: radial-gradient(circle, #d9a070 0%, #b97a4a 55%, transparent 70%); }
  .art-cat-left { left: 45px; top: 480px; width: 130px; height: 130px;
    background: radial-gradient(circle, #9c9c9c 0%, #6e6e6e 55%, transparent 70%); }

  .headline-box { position: absolute; left: 240px; top: 85px; width: 370px; height: 128px;
    background: var(--green); border: 7px solid var(--orange); border-radius: 36px;
    display: flex; flex-direction: column; justify-content: center; align-items: center;
    color: var(--white); font-weight: 800; font-size: 34px; line-height: 1.25; }

  .date { position: absolute; top: 335px; left: 0; width: 100%; text-align: center;
    font-weight: 800; font-size: 38px; }
  .date .num { color: var(--red); font-size: 54px; }

  .closed-band { position: absolute; left: 90px; top: 400px; width: 670px; height: 76px;
    background: var(--green); color: var(--white);
    font-weight: 800; font-size: 50px; text-align: center; line-height: 76px; }
  .closed-band .small { font-size: 38px; }

  .all-days { position: absolute; top: 488px; left: 0; width: 100%; text-align: center;
    font-weight: 800; font-size: 100px; line-height: 1.1; color: var(--green);
    text-shadow: 4px 4px 0 var(--white), -4px -4px 0 var(--white), 4px -4px 0 var(--white), -4px 4px 0 var(--white),
      0 4px 0 var(--white), 0 -4px 0 var(--white), 4px 0 0 var(--white), -4px 0 0 var(--white); }
  .change { position: absolute; top: 600px; left: 0; width: 100%; text-align: center;
    font-weight: 800; font-size: 48px; line-height: 1.1; color: var(--green-dark); }
  .except { position: absolute; top: 662px; left: 0; width: 100%; text-align: center;
    font-weight: 700; font-size: 20px; }

  .clinic { position: absolute; left: 36px; top: 792px; width: 410px; }
  .clinic-name { font-weight: 800; font-size: 30px; line-height: 1.2; }
  .doctors { margin-top: 8px; font-size: 21px; font-weight: 700; }
  .doctors .role { color: var(--brown); }
  .tel { margin-top: 6px; display: flex; align-items: center; gap: 8px; }
  .tel-label { background: var(--red); color: var(--white); font-weight: 800; font-size: 18px;
    padding: 2px 6px; border-radius: 5px; }
  .tel-number { font-weight: 800; font-size: 40px; color: var(--green-dark); line-height: 1.1; }
  .address { margin-top: 6px; font-size: 13px; }
  .hours { margin-top: 8px; border-collapse: collapse; font-size: 14px; }
  .hours th { background: var(--green); color: var(--white); font-weight: 700;
    padding: 3px 8px; border: 2px solid var(--white); }
  .hours td { padding: 3px 10px; font-weight: 700; }
  .hours .note { color: var(--red); border: 2px solid var(--red); font-size: 13px; text-align: center; }

  .map { position: absolute; left: 455px; top: 720px; width: 250px; height: 305px;
    background: linear-gradient(160deg, #ffffff, #f1ece4); border: 2px solid #d8cdbd; border-radius: 4px; }
  .sign-photo { position: absolute; left: 718px; top: 720px; width: 95px; height: 120px;
    background: linear-gradient(180deg, #3d4a5c, #6a7a8c); border-radius: 4px; }

  .parking { position: absolute; left: 455px; top: 1042px; width: 370px; font-size: 14px;
    font-weight: 700; line-height: 1.6; }
  .parking .hl { color: var(--red); }
</style>
</head>
<body>
<div class="flyer">
  <div class="art art-dog" role="img" aria-label="犬のイラスト"></div>
  <div class="art art-cat-right" role="img" aria-label="猫のイラスト"></div>
  <div class="art art-cat-left" role="img" aria-label="猫のイラスト"></div>

  <div class="headline-box">
    <span>動物病院ひだまり</span>
    <span>若草台からお知らせ</span>
  </div>

  <p class="date">2020年<span class="num">2</span>月<span class="num">1</span>日より</p>
  <p class="closed-band">木曜日休診<span class="small">が</span></p>
  <p class="all-days">全曜日診察</p>
  <p class="change">に変わります</p>
  <p class="except">（盆、年末年始、GW は除く）</p>

  <section class="clinic">
    <h1 class="clinic-name">動物病院ひだまり　若草台</h1>
    <p class="doctors"><span class="role">院長</span> 青柳航平　<span class="role">副院長</span> 村瀬譲</p>
    <p class="tel"><span class="tel-label">TEL</span><span class="tel-number">075-614-7328</span></p>
    <p class="address">〒615-8099 京都市西京区小川原南町17 メゾン葵野2階</p>
    <table class="hours">
      <tr><th>診察時間</th><td>午前 9：30〜12：30</td><td class="note" rowspan="2">日、祝日は<br>午前のみ</td></tr>
      <tr><th>予約診察</th><td>16：00〜16：45</td></tr>
      <tr><th>診察時間</th><td>午後 17：00〜20：00</td><td class="note">全曜日診察</td></tr>
    </table>
  </section>

  <div class="map" role="img" aria-label="駐車場と病院の位置を示す地図"></div>
  <div class="sign-photo" role="img" aria-label="病院の看板（暖簾）の写真"></div>

  <div class="parking">
    <p>●駐車場5台完備（トリミングサロン共用）</p>
    <p>●近隣コインパーキングもご利用いただけます</p>
    <p class="hl">No.12,14,19 は当院専用です</p>
  </div>
</div>
</body>
</html>
```